Electrical contractor

looking for a standard sized, horizontal, double sided business card for an electrical contractors business.
i have played around on microsoft word (only computer program i know how to use!) and will attach what i have made so far, really open to any ideas. i just want the DORB to stand out to the rest of the business name.

i wish to use the colours black and green, and white for writing. i will attach the pictures i took off google, i want to either use them, or somethin similar for the back grounds

i wish the front to have the following info:
business name: D.O.R.B ELECTRICAL CONTRACTORS
MY NAME; CORBIN HOLT
STATUS; A CLASS ELECTRICIAN
LICENSE NO; TRN517394
PH NO. 0431576204
EMAIL ADD. DORB.ELECTRICAL@VELTOMAIL.COM
AND MY SLOGAN: where excellence meets integrity, and service comes with a smile.

i am not sure what to have on the back, other than what i do for work.eg titled WHAT WE DO
i dont want too much written on there or will look crowded, but options to add to back, from most important to least, please pick however many you think will look the best
new homes/extentions
led lighting and downlights
Solar Power
power
safety switches
switchboards
telephone and tv
smoke alarms
stoves and ovens
hot water systems
fault finding
re wiring
Updates

Thank you to those who have submitted designs, I would like to change my slogan to something more simple, I'm thinking something like. RELIABLE. EFFICIENT. PROFESSIONAL. AFFORDABLE. in what ever order you thinks fits best. Thanks

Industry/Entity Type

Contractor

```html
<!DOCTYPE html>
<html lang="en">
<head>
<meta charset="utf-8">
<title>D.O.R.B Electrical Consultants – Business Card</title>
<link rel="stylesheet" href="https://fonts.googleapis.com/css2?family=Barlow:wght@300;400;500;600;700&display=swap">
<style>
  :root {
    --paper: #ffffff;
    --card: #070909;
    --neon: #3fe41d;
    --ink: #111111;
    --light: #f2f2f2;
  }
  * { margin: 0; padding: 0; box-sizing: border-box; }
  html, body { width: 1200px; height: 1000px; overflow: hidden; background: var(--paper); }
  body { position: relative; font-family: "Barlow", sans-serif; color: var(--ink); }

  .notes { position: absolute; left: 60px; top: 118px; width: 434px; font-size: 11.5px; line-height: 15.5px; }
  .notes p { text-align: justify; margin-bottom: 16px; }
  .notes .label { color: var(--neon); font-weight: 700; font-size: 13px; }
  .notes .closing { margin-top: 52px; text-transform: uppercase; text-align: left; }

  .card { position: absolute; left: 522px; width: 586px; height: 380px; background: var(--card); }
  .card--front { top: 115px; }
  .card--back { top: 505px; height: 379px; }
  .card__frame { position: absolute; left: 33px; top: 27px; width: 519px; height: 327px; border: 2px solid var(--neon); }
  .card--back .card__frame { top: 26px; width: 520px; }

  .card > span, .card > div { position: absolute; }
  .brand { top: 42px; left: 51px; width: 300px; height: 44px; }
  .brand__letter { position: absolute; top: 0; font-size: 46px; font-weight: 700; color: var(--neon); line-height: 44px; }
  .brand__sub { top: 88px; left: 51px; font-size: 21px; letter-spacing: 0.5px; color: var(--light); font-weight: 400; }
  .slogan { top: 145px; left: 45px; font-size: 16px; font-weight: 300; color: var(--neon); }
  .person { top: 230px; left: 49px; font-size: 16px; color: var(--neon); font-weight: 400; letter-spacing: 0.3px; }
  .detail { left: 49px; font-size: 15px; color: var(--light); font-weight: 400; letter-spacing: 0.3px; }

  .services { top: 96px; left: 0; width: 586px; display: grid; grid-template-columns: 278px 300px; column-gap: 22px; row-gap: 6px; font-size: 15px; line-height: 19px; color: var(--light); letter-spacing: 0.3px; }
  .services .left { text-align: right; }
</style>
</head>
<body>
  <section class="notes">
    <p><span class="label">Client:</span> D.O.R.B Electrical Consultants</p>
    <p><span class="label">Brief:</span> Double sided Business Card</p>
    <p><span class="label">Outcome:</span> The client wished to have a green and black colour scheme. After looming at a mock up supplied i understood what the client prefered to a design.</p>
    <p>I decided to not include the green light shown in the pictures provided as it was designed another design an could claim copyright on its use in the final design.</p>
    <p>To get passed this i chosen a neon green colour it will create the same effect as a light.</p>
    <p>On the back I included the information required on the discription on jobs Idid so in a way that clearly demonstrates them and does not look confusing.</p>
    <p><span class="label">Summary:</span> I believe this design looks very proffesional and could help attract a broad range of clients for DORB Electrical Conultants</p>
    <p class="closing">All designs can be altered if you have any problems the design.<br>Thank you for this oppertunity and I hope you like my design.</p>
  </section>

  <article class="card card--front">
    <div class="card__frame"></div>
    <div class="brand">
      <span class="brand__letter" style="left:0">D</span>
      <span class="brand__letter" style="left:86px">O</span>
      <span class="brand__letter" style="left:172px">R</span>
      <span class="brand__letter" style="left:262px">B</span>
    </div>
    <span class="brand__sub">ELECTRICAL CONSULTANTS</span>
    <span class="slogan">“Where excelence meets integrity and service comes with a smile”</span>
    <span class="person">CORBIN HOLT</span>
    <span class="detail" style="top:252px">A class Electrician</span>
    <span class="detail" style="top:271px">Lisence Number: TRN517394</span>
    <span class="detail" style="top:299px">0431576204</span>
    <span class="detail" style="top:320px">dorb.electrical@veltomail.com</span>
  </article>

  <article class="card card--back">
    <div class="card__frame"></div>
    <div class="services">
      <span class="left">STOVES AND OVENS</span><span>HOT WATER SYSTEMS</span>
      <span class="left">SAFETY SWITCHES</span><span>HOME EXTENTIONS</span>
      <span class="left">SMOKE ALARMS</span><span>SWITCHBOARDS</span>
      <span class="left">FAULT FINDING</span><span>SOLAR POWER</span>
      <span class="left">DOWN LIGHTS</span><span>TELEVISONS</span>
      <span class="left">TELEPHONES</span><span>LED LIGHTS</span>
      <span class="left">NEW HOMES</span><span>RE-WIRING</span>
    </div>
  </article>
</body>
</html>
```